Clean professional design needed for landscape property business

We need a logo for a new lawncare, landscaping , property maintenance business called Meadow Trim.
Our services include lawn mowing, garden maintenance, clean ups and some property maintenance.
We want a double sided business card that is clean and very professional using the colour scheme from our logo which is provided.
the business card should have impact as we will use these to drop into people's letterboxes as a marketing drop.
Initially we want to see what you come up with so there is a very wide scope here to work with.
Updates

Project Deadline Extended
Reason: we feel our original deadline was too short. we have extended to give more time for quality submissions.

Target Market(s)

High end property owners who don't wish to do there own gardneing or property maintenance

Industry/Entity Type

Business

Contact Information for Business Card

Name
Postion/ Title
Phone number
mobile
web address
physical address

services offered

Font styles to use
Sans Serif

Requirements
Must have
• curved edges preferrred
Nice to have
• We like the idea of the logo being embossed or etched into the card so it looks like it is below the surface of the card
Should not have
• No stock images or characters.

```html
<!DOCTYPE html>
<html lang="en">
<head>
<meta charset="utf-8">
<title>Meadow Trim business card</title>
<link rel="stylesheet" href="https://fonts.googleapis.com/css2?family=Source+Sans+3:wght@400;600&display=swap">
<style>
  :root {
    --stage: #000000;
    --card: #f9f9f9;
    --brand-red: #e0092a;
    --brand-green: #80bc00;
    --ink: #111111;
    --white: #ffffff;
  }
  * { margin: 0; padding: 0; box-sizing: border-box; }
  html, body {
    width: 1200px; height: 1200px; overflow: hidden;
    background: var(--stage);
    font-family: "Source Sans 3", sans-serif;
  }
  .canvas { position: relative; width: 1200px; height: 1200px; }
  .card {
    position: absolute; left: 193px; width: 850px; height: 520px;
    background: var(--card); overflow: hidden;
  }
  .card--front { top: 34px; }
  .card--back { top: 612px; }

  .accent-bar {
    position: absolute; left: 0; top: 0; width: 366px; height: 22px;
    background: var(--brand-red);
  }
  .brand {
    position: absolute; display: flex; align-items: center; gap: 10px;
    color: var(--brand-red); font-weight: 400; letter-spacing: 2px; white-space: nowrap;
  }
  .brand__dot { border-radius: 50%; background: var(--brand-green); flex: none; }
  .card--front .brand { right: 108px; top: 150px; font-size: 38px; }
  .card--front .brand__dot { width: 16px; height: 16px; }
  .card--back .brand { left: 50%; transform: translateX(-50%); top: 276px; font-size: 56px; }
  .card--back .brand__dot { width: 22px; height: 22px; }

  .person { position: absolute; left: 72px; top: 218px; color: var(--ink); }
  .person__name { font-size: 28px; line-height: 1; }
  .person__title { font-size: 16px; line-height: 1.2; }

  .address { position: absolute; left: 226px; top: 330px; font-size: 21px; color: var(--ink); }
  .divider {
    position: absolute; left: 421px; top: 331px; width: 2px; height: 101px;
    background: var(--brand-red);
  }
  .contact { position: absolute; left: 442px; top: 348px; font-size: 21px; color: var(--ink); line-height: 27px; }
  .contact__label { color: var(--brand-red); display: inline-block; width: 34px; }

  .services-band {
    position: absolute; left: 0; top: 451px; width: 100%; height: 69px;
    background: var(--brand-green); color: var(--white);
    display: flex; align-items: center; justify-content: center; font-size: 17px;
  }

  .website {
    position: absolute; left: 0; width: 100%; top: 464px; text-align: center;
    font-size: 22px; color: var(--ink);
  }
</style>
</head>
<body>
<div class="canvas">
  <section class="card card--front">
    <div class="accent-bar"></div>
    <div class="brand"><span class="brand__dot"></span>MEADOW TRIM</div>
    <div class="person">
      <p class="person__name">Name</p>
      <p class="person__title">Postion/ Title</p>
    </div>
    <p class="address">physical address</p>
    <div class="divider"></div>
    <div class="contact">
      <p><span class="contact__label">P &nbsp;:</span>06001 2345</p>
      <p><span class="contact__label">m :</span>03 55501 23456</p>
    </div>
    <div class="services-band">lawn mowing, garden maintenance, clean ups and some property maintenance</div>
  </section>

  <section class="card card--back">
    <div class="brand"><span class="brand__dot"></span>MEADOW TRIM</div>
    <p class="website">www.meadowtrim.com</p>
  </section>
</div>
</body>
</html>
```